Luxury Inclusive Beauty Brand Needs Labels & Boxes for Product Line

We need updated labels and boxes for our cosmetic and skin care line. Our company is MAVRA & CO. and we focus on providing upscale, natural and organic beauty products inclusive of diverse and deeper skin tones for women of color, especially black women. We have a seven piece skin care collection called DERMAVELLE Baobin Collection and a mineral make-up line consisting of eight products. The design of all products should be the same with just dimensions and title/ingredient list differences. We would like to see designs that use our coral color e85350, work well on black packaging (bottles, lipstick tubes etc.) and include white and other additional pretty colors, metallics or patterns representative of ethnic (AFRICAN), bohemian or tribal influence. The final design should communicate luxury, floral/fauna environmentalism, and afrocentric culture influences.
We have included files of various prints we like and the type of lifestyle our customer aspires to/is attracted to. We have included in the files below some examples of packaging we like but we want something original to capture the attention of our target market, upper income health and ethnic conscious black women age 30 - 55 who love natural and organic products. The names of our products include the list below however if design can be submitted showing design on 1 tall box and 1 short box and 1 lipstick size box that would be great:
DERMAVELLE Baobin Collection Cleansing Oil (dropper)
DERMAVELLE Baobin Collection Balancing Toner (tall spray bottle)
DERMAVELLE Baobin Collection Moisturizing Serum (dropper)
DERMAVELLE Baobin Collection Moisturizing Cream (short box jar)
DERMAVELLE Baobin Lip Scrub (short box - jar)
Luminous Mineral Foundation (short box- jar)
CC Cream
Moisturizing Lip Stick (lipstick box)
OTIRAFLIX Natural Mascara
Zarra Bimble Lip Crayon
Gel Eye Liner
Organic Make-up Remover (tall spray bottle)
Face & Eye Primer
Final dimensions /dies of boxes can be sent to winner of design competition.
Target Market(s)
women of color, age 30-55, income 50 - 150K, natural hair and organic lifestyle, yoga
Industry/Entity Type
Cosmetics
Requirements
Must have
- label and box
- include the color e85350
- include logo
Nice to have
- easy way to differentiate skincare from make-up products

```html
<!DOCTYPE html>
<html lang="en">
<head>
<meta charset="utf-8">
<title>MAVRA &amp; CO. – Baobin Collection Packaging</title>
<link rel="stylesheet" href="https://fonts.googleapis.com/css2?family=Abel&family=Montserrat:wght@300;400&family=Mr+Dafoe&display=swap">
<style>
  :root {
    --coral: #e85350;
    --coral-deep: #d4504e;
    --coral-muted: #cf5653;
    --coral-bright: #f2524f;
    --white: #ffffff;
    --page: #ffffff;
  }
  * { margin: 0; padding: 0; box-sizing: border-box; }
  html, body {
    width: 1137px;
    height: 1200px;
    overflow: hidden;
    background: var(--page);
  }
  .canvas {
    position: relative;
    width: 1137px;
    height: 1200px;
  }
  .panel {
    position: absolute;
    overflow: hidden;
    color: var(--white);
    text-align: center;
  }
  .panel__pattern {
    position: absolute;
    inset: 0;
  }
  .panel__item {
    position: absolute;
    left: 0;
    right: 0;
    display: flex;
    justify-content: center;
  }

  .logo-mark {
    border: 1.5px solid var(--white);
    border-radius: 50%;
  }
  .brand-name {
    font-family: "Abel", sans-serif;
    font-weight: 400;
    letter-spacing: 0.02em;
    white-space: nowrap;
  }
  .collection-name {
    font-family: "Montserrat", sans-serif;
    font-weight: 300;
    text-transform: lowercase;
    white-space: nowrap;
  }
  .product-title {
    font-family: "Mr Dafoe", cursive;
    font-weight: 400;
    white-space: nowrap;
    transform: rotate(-4deg);
  }

  /* Dropper bottle label */
  .bottle-label {
    left: 192px;
    top: 583px;
    width: 263px;
    height: 418px;
  }
  .bottle-label .panel__pattern {
    background:
      radial-gradient(circle at 30% 25%, var(--coral-bright) 0, transparent 45%),
      radial-gradient(circle at 75% 80%, var(--coral-bright) 0, transparent 40%),
      var(--coral-muted);
  }
  .bottle-label .logo-slot { top: 30px; }
  .bottle-label .logo-mark { width: 40px; height: 40px; }
  .bottle-label .brand-slot { top: 82px; }
  .bottle-label .brand-name { font-size: 21px; }
  .bottle-label .collection-slot { top: 134px; }
  .bottle-label .collection-name {
    font-size: 20px;
    line-height: 1.45;
    letter-spacing: 0.42em;
    padding-left: 0.42em;
  }
  .bottle-label .title-slot { top: 204px; }
  .bottle-label .product-title { font-size: 54px; line-height: 1.4; }

  /* Lipstick box front */
  .lipstick-box {
    left: 500px;
    top: 160px;
    width: 272px;
    height: 945px;
  }
  .lipstick-box .panel__pattern {
    background:
      radial-gradient(circle at 25% 15%, var(--coral-bright) 0, transparent 35%),
      radial-gradient(circle at 80% 55%, var(--coral-bright) 0, transparent 35%),
      radial-gradient(circle at 35% 90%, var(--coral-bright) 0, transparent 30%),
      var(--coral-deep);
  }
  .lipstick-box .logo-slot { top: 74px; }
  .lipstick-box .logo-mark { width: 52px; height: 52px; }
  .lipstick-box .brand-slot { top: 136px; }
  .lipstick-box .brand-name { font-size: 26px; }
  .lipstick-box .collection-slot { top: 200px; }
  .lipstick-box .collection-name {
    font-size: 27px;
    line-height: 1.3;
    letter-spacing: 0.38em;
    padding-left: 0.38em;
  }
  .lipstick-box .title-slot { top: 446px; }
  .lipstick-box .product-title { font-size: 52px; line-height: 1.5; }
</style>
</head>
<body>
<main class="canvas">
  <section class="panel bottle-label">
    <div class="panel__pattern" role="img" aria-label="Coral botanical floral pattern"></div>
    <div class="panel__item logo-slot"><span class="logo-mark"></span></div>
    <div class="panel__item brand-slot"><p class="brand-name">MAVRA &amp; CO.</p></div>
    <div class="panel__item collection-slot"><p class="collection-name">baobin<br>collection</p></div>
    <div class="panel__item title-slot"><h1 class="product-title">Cleansing<br>Oil</h1></div>
  </section>

  <section class="panel lipstick-box">
    <div class="panel__pattern" role="img" aria-label="Coral botanical floral pattern"></div>
    <div class="panel__item logo-slot"><span class="logo-mark"></span></div>
    <div class="panel__item brand-slot"><p class="brand-name">MAVRA &amp; CO.</p></div>
    <div class="panel__item collection-slot"><p class="collection-name">baobin<br>collection</p></div>
    <div class="panel__item title-slot"><h2 class="product-title">Moisturizing<br>Lip Stick</h2></div>
  </section>
</main>
</body>
</html>
```